A sustainable tourism website

We are a travel/tourism company. We have developed a platform that enables organizers of sustainable theme vacations to publish and make their vacations bookable via our platform. By theme vacations, we mean vacations in categories such as Wellness, Surfing, Culinary, Martial arts, etc. We already have separate websites for each of these categories. This new website you will design is about a parent site where we provide general summary information about these individual sites and link to them. The site would be hosted on the domain velmarogo.net. Besides information about the individual sites, we also need a menu for About Us, Products and Our Climate Pledge. We also need the following at the home page:
1. A section that contain our last tweets in a twitter lightbox.
2. Summary and links to of our last few blogs.
3. A video as banner or an image. We would prefer a video though.
We already have a logo and have uploaded it. Please make sure your design conforms with our logo style and colors.
NB: We are looking for something more than the standard site you see everywhere. The winning design is a design that stands out and has a WOW effect. And when your design is selected, we intend to work with you further for the completion of the whole site.

Target Market(s)

Sustainable tourism

Number of Pages Required

1 page

Requirements
Must have
• Conform to logo design and colors.
Site must be unique, slick and stand out.
Must have a climate/sustainability blended with tourism look.
Nice to have
• Video as banner.

```html
<!DOCTYPE html>
<html lang="en">
<head>
<meta charset="utf-8">
<title>Velmarogo – Sustainable Theme Vacations</title>
<link rel="stylesheet" href="https://fonts.googleapis.com/css2?family=Lora:wght@400&family=Nunito+Sans:wght@300;400;600;700&display=swap">
<style>
:root{
  --yellow:#f5c422;
  --orange:#f0a02b;
  --ink:#1f2226;
  --text:#4a4d52;
  --muted:#9a9da2;
  --line:#ececec;
  --white:#ffffff;
}
*{margin:0;padding:0;box-sizing:border-box}
html,body{width:1200px;height:3198px;overflow:hidden;background:var(--white)}
body{position:relative;font-family:"Nunito Sans",sans-serif;color:var(--text)}
.abs{position:absolute}
.serif{font-family:"Lora",serif;font-weight:400;color:var(--ink)}

/* hero */
.hero{left:0;top:0;width:1200px;height:600px;
  background:linear-gradient(180deg,#f3c77a 0%,#c99a55 22%,#7d7048 45%,#4f6a55 65%,#8aa04a 85%,#6b8a3e 100%)}
.brand{font-size:22px;font-weight:400;color:var(--orange);display:flex;align-items:center;gap:6px}
.brand::after{content:"";width:10px;height:10px;border-radius:50%;background:var(--orange)}
.nav{top:38px;left:0;width:1200px}
.nav a{position:absolute;font-size:12px;font-weight:600;color:#3a3020;text-decoration:none;letter-spacing:.3px}
.hero-title{left:0;width:1200px;top:205px;text-align:center;font-size:58px;line-height:68px;color:var(--white)}

/* sections */
.h2{font-size:30px;left:100px}
.trip{top:826px;width:283px;height:434px;border-radius:6px;overflow:hidden;color:var(--white)}
.trip .tag{position:absolute;left:27px;top:50px;font-size:12px;letter-spacing:4px}
.trip .name{position:absolute;left:27px;top:292px;font-size:28px;font-weight:600}
.trip .desc{position:absolute;left:27px;top:348px;width:235px;font-size:15px;line-height:18px;font-weight:300}

.tab{top:1514px;font-size:19px}
.btn{background:var(--yellow);color:var(--white);font-weight:700;font-size:14px;border-radius:8px;display:flex;align-items:center;justify-content:center}

.tweet{left:633px;top:1427px;width:467px;height:412px;border-radius:12px;background:var(--white);box-shadow:0 4px 22px rgba(0,0,0,.09)}

.post{top:2025px;width:467px;height:411px;border-radius:10px;overflow:hidden;background:var(--white);box-shadow:0 4px 22px rgba(0,0,0,.08)}
.post .img{height:266px}
.post h3{position:absolute;left:27px;top:290px;font-size:18px;font-weight:700;color:var(--ink)}
.post p{position:absolute;left:27px;top:328px;font-size:16px;color:var(--text)}
.post a{position:absolute;left:27px;top:374px;font-size:15px;font-weight:700;color:#3a3d42;text-decoration:none}

.foot a{position:absolute;font-size:11px;color:#6a6d72;text-decoration:none;letter-spacing:.3px}
.social{top:3075px;width:18px;height:18px;border:1.4px solid #b8bbc0;border-radius:4px}
</style>
</head>
<body>

<!-- hero -->
<div class="abs hero" role="img" aria-label="Video banner: a surfer riding a wave at golden sunset"></div>
<div class="abs brand" style="left:100px;top:32px">velmarogo</div>
<nav class="abs nav">
  <a style="left:687px" href="#">HOME</a>
  <a style="left:775px" href="#">ABOUT US</a>
  <a style="left:887px" href="#">PRODUCT</a>
  <a style="left:998px" href="#">CLIMATE PLEDGE</a>
</nav>
<h1 class="abs serif hero-title" style="color:var(--white)">Lorem ipsum dolor<br>sit amet</h1>
<svg class="abs" style="left:569px;top:359px" width="62" height="62" viewBox="0 0 62 62">
  <circle cx="31" cy="31" r="29" fill="none" stroke="#fff" stroke-width="2"/>
  <path d="M25 21 L41 31 L25 41 Z" fill="#fff"/>
</svg>
<svg class="abs" style="left:586px;top:463px" width="28" height="42" viewBox="0 0 28 42">
  <rect x="1.5" y="1.5" width="25" height="39" rx="12.5" fill="none" stroke="#fff" stroke-width="1.6"/>
  <path d="M14 12 V28 M9 23 L14 28 L19 23" fill="none" stroke="#fff" stroke-width="1.6"/>
</svg>

<!-- trips -->
<h2 class="abs serif h2" style="top:762px">First-class Trips are Waiting for You!</h2>
<div class="abs trip" style="left:100px;background:linear-gradient(180deg,#8a8f96,#c9ccd1 60%,#4d5258)" role="img" aria-label="Martial art students in white uniforms">
  <span class="tag">MARTIAL ART</span><span class="name">KARATE</span><span class="desc">Ultricies interdum massa vel sem cursus mauris.</span></div>
<div class="abs trip" style="left:410px;background:linear-gradient(180deg,#7d8a96,#3f7f86 55%,#2b3a46)" role="img" aria-label="Yoga class stretching outdoors">
  <span class="tag">WELLNESS</span><span class="name">YOGA</span><span class="desc">Nisi, maecenas arcu, tempor sed lectus rhoncus.</span></div>
<div class="abs trip" style="left:720px;background:linear-gradient(180deg,#8f9297,#e3a13a 40%,#8b7a4a 70%,#d8d8d8)" role="img" aria-label="Plated scallops with greens and sauce">
  <span class="tag">CULINARY</span><span class="name">FOOD</span><span class="desc">Ultricies interdum massa vel sem cursus mauris.</span></div>
<div class="abs trip" style="left:1030px;background:linear-gradient(180deg,#3d8fa6,#1f6e88 55%,#7ba2b4)" role="img" aria-label="Surfer on a blue wave">
  <span class="tag">SPORT</span><span class="name">SURFING</span><span class="desc" style="width:250px">Ultricies interdum massa vel sem cursus mauris.</span></div>

<!-- latest information -->
<h2 class="abs serif h2" style="top:1460px">Get the Latest&nbsp; Information</h2>
<span class="abs tab" style="left:100px;color:var(--yellow)">About Us</span>
<span class="abs tab" style="left:250px;color:var(--muted)">Why Choose Us</span>
<div class="abs" style="left:100px;top:1545px;width:104px;height:4px;background:var(--yellow)"></div>
<p class="abs" style="left:100px;top:1572px;width:330px;font-size:16px;line-height:18px">Magnis sed integer eget nisi egestas tellus id a. Sollicitudin proin morbi mi faucibus a commodo</p>
<a class="abs btn" href="#" style="left:100px;top:1710px;width:152px;height:58px;text-decoration:none">Get in touch</a>

<div class="abs tweet">
  <div class="abs" style="left:35px;top:27px;width:40px;height:40px;border-radius:50%;background:#fbf1cf"></div>
  <div class="abs" style="left:84px;top:32px;font-size:12px;font-weight:700;color:var(--ink)">velmarogo</div>
  <div class="abs" style="left:84px;top:46px;font-size:11px;color:var(--muted)">@velmarogo</div>
  <p class="abs" style="left:35px;top:86px;width:400px;font-size:13px;line-height:23px;color:var(--muted)">Amet sit adipiscing quam ipsum ullamcorper ut. Id pulvinar sapien, id fames sagittis ut magna ac in. Arcu pharetra.</p>
  <div class="abs" style="left:35px;top:160px;width:397px;height:155px;border-radius:12px;background:linear-gradient(100deg,#1b6f86,#26a6b8 45%,#e8dccb 70%,#b9b0a0)" role="img" aria-label="Turquoise cove beneath limestone cliffs"></div>
  <div class="abs" style="left:37px;top:335px;font-size:10px;color:var(--muted)">05:19 AM.Oct 24</div>
  <div class="abs" style="left:35px;top:361px;width:397px;height:1px;background:var(--line)"></div>
  <svg class="abs" style="left:36px;top:373px" width="14" height="13" viewBox="0 0 14 13"><path d="M7 12 L1.5 6.5 A3 3 0 0 1 7 2.5 A3 3 0 0 1 12.5 6.5 Z" fill="none" stroke="#9a9da2" stroke-width="1.2"/></svg>
  <span class="abs" style="left:58px;top:373px;font-size:10px;color:var(--muted)">215</span>
  <svg class="abs" style="left:94px;top:373px" width="14" height="13" viewBox="0 0 14 13"><path d="M2 10 L3 7.5 A5 4.5 0 1 1 5 10 Z" fill="none" stroke="#9a9da2" stroke-width="1.2"/></svg>
  <span class="abs" style="left:116px;top:373px;font-size:10px;color:var(--muted)">102 people are Tweeting about this</span>
</div>

<!-- blog -->
<h2 class="abs serif h2" style="top:1962px">Latest Blog Posts</h2>
<article class="abs post" style="left:100px">
  <div class="img" style="background:linear-gradient(180deg,#b9d3dc,#3f9fae 40%,#126d82)" role="img" aria-label="Swimmer near a green island in clear sea"></div>
  <h3>Lorem Ipsum</h3><p>Sollicitudin proin morbi mi faucibus a commodo</p><a href="#">Read more</a>
</article>
<article class="abs post" style="left:633px">
  <div class="img" style="background:linear-gradient(180deg,#d9d5cc,#8a6a3e 40%,#c9a25a 60%,#5f8a34)" role="img" aria-label="Grilled fish with diced fruit and broccoli"></div>
  <h3>Dolor sit amet</h3><p>Sollicitudin proin morbi mi faucibus a commodo</p><a href="#">Read more</a>
</article>
<article class="abs post" style="left:1166px">
  <div class="img" style="background:linear-gradient(180deg,#9fb8bf,#b9a98a)" role="img" aria-label="Sandy beach with rocks"></div>
  <h3>D</h3><p>S</p><a href="#">R</a>
</article>

<!-- newsletter -->
<h2 class="abs serif" style="left:0;width:1200px;top:2600px;text-align:center;font-size:30px">Sign up to Our Newsletter</h2>
<p class="abs" style="left:440px;top:2662px;width:320px;text-align:center;font-size:16px;line-height:18px">Magnis sed integer eget nisi egestas tellus id a. Sollicitudin proin morbi mi faucibus a commodo</p>
<div class="abs" style="left:355px;top:2760px;width:321px;height:57px;border-radius:6px;background:var(--white);box-shadow:0 3px 14px rgba(0,0,0,.08);font-size:10px;color:#c8cace;padding:24px 0 0 26px">Enter Your Email</div>
<a class="abs btn" href="#" style="left:694px;top:2760px;width:151px;height:57px;text-decoration:none">Sign up</a>

<!-- footer -->
<div class="abs" style="left:100px;top:2941px;width:1000px;height:1px;background:var(--line)"></div>
<div class="abs brand" style="left:100px;top:3010px;font-size:28px">velmarogo</div>
<div class="abs social" style="left:101px"></div>
<div class="abs social" style="left:151px"></div>
<div class="abs social" style="left:200px"></div>
<div class="abs social" style="left:250px"></div>
<nav class="abs foot" style="left:0;top:0">
  <a style="left:439px;top:3021px" href="#">HOME</a>
  <a style="left:608px;top:3021px" href="#">FAQ</a>
  <a style="left:762px;top:3021px" href="#">PLANING</a>
  <a style="left:931px;top:3021px" href="#">BLOG</a>
  <a style="left:439px;top:3078px" href="#">TRIPS</a>
  <a style="left:608px;top:3078px" href="#">GUIDES</a>
  <a style="left:762px;top:3078px" href="#">ABOUT</a>
  <a style="left:931px;top:3078px" href="#">CONTACT</a>
</nav>
<div class="abs" style="left:0;width:1200px;top:3166px;text-align:center;font-size:9px;color:#b8bbc0">Copyright © Velmarogo</div>

</body>
</html>
```